Ridgemont Business Card Redesign

Using the current logo/tagline lock-up and icon, redesign the Ridgemont business card to better show the tagline and improve the layout to give the card a more timely design and a classic, sophisticated look. See attached Project Brief for more detail.

```html
<!DOCTYPE html>
<html lang="en">
<head>
<meta charset="utf-8">
<title>Ridgemont Capital – Business Card</title>
<link href="https://fonts.googleapis.com/css2?family=Lato:wght@400;700&display=swap" rel="stylesheet">
<style>
  :root {
    --page-bg: #ffffff;
    --card-bg: #efefee;
    --brand-blue: #1a70b9;
    --brand-dark: #444547;
    --text-main: #3a3a3b;
    --rule: #555658;
  }
  * { box-sizing: border-box; margin: 0; padding: 0; }
  html, body {
    width: 1200px; height: 840px; overflow: hidden;
    background: var(--page-bg);
    font-family: "Lato", Arial, sans-serif;
    color: var(--text-main);
  }
  .card {
    position: absolute; left: 180px; top: 180px;
    width: 840px; height: 480px;
    background: var(--card-bg);
    border-radius: 32px;
    overflow: hidden;
  }
  .brand {
    position: absolute; left: 0; right: 0; top: 92px;
    display: flex; flex-direction: column; align-items: center;
  }
  .brand-lockup { display: flex; align-items: center; gap: 16px; }
  .brand-dot {
    width: 34px; height: 34px; border-radius: 50%;
    background: var(--brand-blue);
  }
  .brand-name {
    font-size: 40px; font-weight: 700; letter-spacing: 3px;
    text-transform: uppercase; color: var(--brand-dark);
  }
  .brand-tagline {
    margin-top: 10px; padding-top: 6px;
    border-top: 1px solid var(--rule);
    font-size: 13px; font-weight: 700; letter-spacing: 2px;
    text-transform: uppercase; color: var(--brand-blue);
  }
  .person {
    position: absolute; right: 452px; top: 262px;
    text-align: right; font-size: 20.5px; line-height: 24px;
  }
  .person-name {
    font-size: 30px; line-height: 36px; color: var(--brand-blue);
    margin-bottom: 2px;
  }
  .divider {
    position: absolute; left: 414px; top: 272px;
    width: 1.5px; height: 120px; background: var(--rule);
  }
  .contacts {
    position: absolute; left: 444px; top: 266px;
    list-style: none; font-size: 20.5px; line-height: 24.3px;
  }
  .contacts li { display: flex; align-items: center; gap: 12px; }
  .contacts svg { width: 18px; height: 18px; fill: var(--brand-blue); flex: none; }
  .band { position: absolute; top: 448px; height: 32px; }
  .band-blue { left: 0; width: 414px; background: var(--brand-blue); }
  .band-dark { left: 420px; right: 0; background: var(--brand-dark); }
</style>
</head>
<body>
  <div class="card">
    <header class="brand">
      <div class="brand-lockup">
        <span class="brand-dot"></span>
        <span class="brand-name">Ridgemont Capital</span>
      </div>
      <div class="brand-tagline">Non-Control Growth Capital</div>
    </header>

    <div class="person">
      <div class="person-name">Daniel Hartley</div>
      <div>Founder &amp; CEO</div>
      <div>48 Harbour Lane</div>
      <div>Suite# B, London</div>
      <div>UK 2047C5</div>
    </div>

    <div class="divider"></div>

    <ul class="contacts">
      <li>
        <svg viewBox="0 0 24 24"><path d="M6.6 10.8a15.1 15.1 0 0 0 6.6 6.6l2.2-2.2a1 1 0 0 1 1-.25 11.4 11.4 0 0 0 3.6.57 1 1 0 0 1 1 1V20a1 1 0 0 1-1 1A17 17 0 0 1 3 4a1 1 0 0 1 1-1h3.5a1 1 0 0 1 1 1c0 1.25.2 2.45.57 3.57a1 1 0 0 1-.25 1z"/></svg>
        000 000 0000 (Direct)
      </li>
      <li>
        <svg viewBox="0 0 24 24"><path d="M2 8c0-2 4-4 10-4s10 2 10 4v2h-5V8.5c-1.5-.6-3-.8-5-.8s-3.5.2-5 .8V10H2z"/><path d="M5 12h14l1 8H4z"/><circle cx="12" cy="16" r="2.2" fill="#efefee"/></svg>
        000 000 0000 (Main)
      </li>
      <li>
        <svg viewBox="0 0 24 24"><path d="M7 1h10a2 2 0 0 1 2 2v18a2 2 0 0 1-2 2H7a2 2 0 0 1-2-2V3a2 2 0 0 1 2-2zm0 3v14h10V4z"/><circle cx="12" cy="20.5" r="1"/></svg>
        000 000 0000
      </li>
      <li>
        <svg viewBox="0 0 24 24"><path d="M2 5h20v14H2z"/><path d="M2 5l10 8 10-8M2 19l7-7M22 19l-7-7" fill="none" stroke="#efefee" stroke-width="1.6"/></svg>
        info@ridgemontcapital.com
      </li>
      <li>
        <svg viewBox="0 0 24 24"><circle cx="12" cy="12" r="10"/><path d="M2 12h20M12 2c3 3 3 17 0 20M12 2c-3 3-3 17 0 20" fill="none" stroke="#efefee" stroke-width="1.4"/></svg>
        www.ridgemontcapital.com
      </li>
    </ul>

    <div class="band band-blue"></div>
    <div class="band band-dark"></div>
  </div>
</body>
</html>
```